design a construction company business card

Design business card around our logo. Card must have all the typical info: name, title, address, phone, email, business name, etc. Somewhere on the card I would like to see our motto "Built on integrity... Inspired by commitment." Consider adding a splash of bright orange to the card to complement the blues and silvers/grays in the logo. We are open to metallic inks, textures, etc. We would like to see options on both light and dark backgrounds. The font in the logo is Euro Technic Extended Regular.

```html
<!DOCTYPE html>
<html lang="en">
<head>
<meta charset="utf-8">
<title>Halden Contracting — Business Card</title>
<link rel="stylesheet" href="https://fonts.googleapis.com/css2?family=Source+Sans+3:wght@400;600&display=swap">
<style>
  :root {
    --backdrop: #e6e4e1;
    --card: #1c1e22;
    --silver: #b9bcc1;
    --white: #f2f2f2;
    --blue: #2f5bd3;
    --rule: #d8d8d8;
  }
  * { margin: 0; padding: 0; box-sizing: border-box; }
  html, body { width: 1200px; height: 864px; overflow: hidden; }
  body {
    background: var(--backdrop);
    font-family: "Source Sans 3", Arial, sans-serif;
    position: relative;
  }
  .card {
    position: absolute;
    width: 540px;
    height: 308px;
    background: var(--card);
    border-radius: 3px;
    box-shadow: 0 6px 18px rgba(0,0,0,.25);
    overflow: hidden;
  }
  /* Back of card */
  .card--back { left: 40px; top: 80px; }
  .card--back .wordmark {
    position: absolute;
    left: 150px; top: 96px;
    display: flex; align-items: center; gap: 12px;
    color: var(--silver);
    font-weight: 600;
    font-size: 40px;
    letter-spacing: 6px;
  }
  .wordmark .mark-square {
    width: 18px; height: 18px; background: currentColor;
  }
  .card--back .wordmark-sub {
    position: absolute;
    left: 180px; top: 150px;
    color: var(--silver);
    font-weight: 600;
    font-size: 14px;
    letter-spacing: 5px;
  }
  .card--back .motto {
    position: absolute;
    left: 60px; top: 220px;
    color: var(--white);
    font-size: 15px;
  }
  /* Front of card */
  .card--front { left: 620px; top: 420px; }
  .contact {
    position: absolute; left: 34px; top: 44px;
    color: var(--white);
  }
  .contact .name {
    color: var(--blue); font-weight: 600; font-size: 18px; letter-spacing: .5px;
  }
  .contact .title { font-size: 13px; margin-bottom: 8px; letter-spacing: .5px; }
  .contact ul { list-style: none; }
  .contact li {
    display: flex; align-items: center; gap: 8px;
    font-size: 14px; line-height: 20px;
  }
  .contact svg { width: 11px; height: 11px; fill: var(--blue); flex: none; }
  .rule {
    position: absolute; height: 1px; background: var(--rule);
  }
  .rule--contact { left: 34px; right: 110px; top: 172px; }
  .rule--address { left: 300px; right: 34px; top: 226px; }
  .card--front .wordmark {
    position: absolute;
    right: 34px; top: 58px;
    display: flex; align-items: center; gap: 10px;
    color: var(--blue);
    font-weight: 600;
    font-size: 34px;
    letter-spacing: 5px;
  }
  .card--front .wordmark-sub {
    position: absolute;
    right: 40px; top: 104px;
    color: var(--white);
    font-weight: 600;
    font-size: 12px;
    letter-spacing: 4px;
  }
  .address {
    position: absolute; right: 34px; top: 240px;
    color: var(--white);
    font-size: 15px; line-height: 20px; text-align: right;
  }
</style>
</head>
<body>
  <section class="card card--back" aria-label="Card back">
    <div class="wordmark"><span class="mark-square"></span>HALDEN</div>
    <div class="wordmark-sub">CONTRACTING, INC.</div>
    <p class="motto">Built on integrity... Inspired by commitment.</p>
  </section>

  <section class="card card--front" aria-label="Card front">
    <div class="contact">
      <div class="name">MARK ELLISON</div>
      <div class="title">PRESIDENT</div>
      <ul>
        <li><svg viewBox="0 0 12 12"><path d="M2 1h3l1 3-1.5 1a7 7 0 0 0 2.5 2.5L8 6l3 1v3a1 1 0 0 1-1 1A9 9 0 0 1 1 2a1 1 0 0 1 1-1z"/></svg>555 0134 2290</li>
        <li><svg viewBox="0 0 12 12"><path d="M0 2h12v8H0z M1 3v.5l5 3.5 5-3.5V3z" fill-rule="evenodd"/></svg>mark@haldenbuild.com</li>
        <li><svg viewBox="0 0 12 12"><circle cx="6" cy="6" r="6"/></svg>www.haldenbuild.com</li>
      </ul>
    </div>
    <div class="rule rule--contact"></div>
    <div class="wordmark"><span class="mark-square"></span>HALDEN</div>
    <div class="wordmark-sub">CONTRACTING, INC.</div>
    <div class="rule rule--address"></div>
    <address class="address" style="font-style:normal">4127 Ashbury Lane<br>Lakeview, NY 11000</address>
  </section>
</body>
</html>
```